KRT Ferravant, LLC. - Georgetown, KY - Chicago, IL

Create a company brochure for KRT Ferravant.
Does process off spec UBC cost you?
-Slower throughput, Double Runs
-Extra Manpower, more picking stations
-Redundant Final Quality Inspections
-Aluminum in the Residue
KRT Ferravant with our Dolvarin Designed and Bulit Custom UBC Specific processing center.
-Guaranteed No Rejections
-Increased cash flow with no rejection delays
-Reduce Manpower Costs
-Increase Total TPH thru your plant
More aluminum recovered - less in your residue
We can eliminate any quality concerns you have with UBC. This will allow you to streamline your operation and concentrate on moving all of your material faster and more efficiently.
We can purchase your baled UBC directly with fast payment or toll process them guaranteeing mill spec.
Target Market(s)
B2B, Waste Recycling Companies, Aluminum Can Recyclers, Aluminum can Brokers, Aluminum Can Mills
Industry/Entity Type
Recycling
Requirements
Nice to have
- You do not have to use the attached photo. It is just an example.

```html
<!DOCTYPE html>
<html lang="en">
<head>
<meta charset="utf-8">
<title>KRT Ferravant Brochure</title>
<link rel="stylesheet" href="https://fonts.googleapis.com/css2?family=Roboto+Condensed:wght@700&family=Lato:wght@400;700&display=swap">
<style>
  :root {
    --bg: #e9e7e2;
    --silver-light: #f4f4f4;
    --silver-mid: #cfcfcf;
    --silver-dark: #a9a9a9;
    --ink: #111111;
    --band-black: #0b0b0b;
    --band-grey: #3a3a3a;
    --green: #3e6a2a;
    --green-dark: #2c4f1d;
    --photo-green: #8fae7e;
    --photo-green-dark: #4f6b44;
    --headline-grey: #bdbdbd;
    --white: #ffffff;
  }
  * { box-sizing: border-box; margin: 0; padding: 0; }
  html, body { width: 1200px; height: 900px; overflow: hidden; }
  body { background: var(--bg); font-family: "Lato", sans-serif; position: relative; }

  .spread { position: absolute; left: 100px; top: 90px; width: 1000px; height: 720px;
    display: flex; box-shadow: 0 6px 24px rgba(0,0,0,.25); }
  .page { position: relative; width: 500px; height: 720px; overflow: hidden; }

  .back-cover { background: linear-gradient(160deg, var(--silver-light) 0%, var(--silver-mid) 55%, var(--silver-dark) 100%); }
  .front-cover { background: linear-gradient(90deg, var(--silver-mid) 0%, var(--silver-light) 40%, var(--white) 60%, var(--silver-mid) 100%); }

  .logo-band { position: absolute; left: 0; top: 182px; width: 100%; height: 225px;
    background: radial-gradient(ellipse at 60% 50%, var(--band-grey) 0%, var(--band-black) 70%);
    display: flex; align-items: center; justify-content: center; }
  .wordmark { font-family: "Lato", sans-serif; font-weight: 700; color: var(--silver-mid); letter-spacing: 2px; }
  .logo-band .wordmark { font-size: 44px; }

  .contact { position: absolute; left: 0; width: 100%; top: 464px; text-align: center; color: var(--ink); font-size: 11.5px; line-height: 1.3; }
  .contact-title { font-weight: 700; font-size: 14px; display: inline-block; padding-bottom: 5px; border-bottom: 1px solid var(--green); margin-bottom: 6px; width: 114px; }
  .contact-phone { font-size: 13px; display: inline-block; padding-bottom: 4px; border-bottom: 1px solid var(--green); margin-bottom: 5px; }
  .contact-line { display: flex; justify-content: center; align-items: center; gap: 4px; }
  .contact-line svg { width: 8px; height: 8px; fill: var(--green-dark); }

  .footer-strip { position: absolute; left: 0; bottom: 0; width: 100%; height: 30px; background: var(--green); }

  .brand-top { position: absolute; top: 55px; left: 0; width: 100%; text-align: center; }
  .brand-top .wordmark { font-size: 40px; color: var(--band-grey); display: block; line-height: 1; }
  .brand-top .subname { font-size: 11px; letter-spacing: 3px; color: var(--band-grey); display: block; margin-top: 6px; }

  .photo { position: absolute; top: 182px; height: 224px; }
  .photo-bales { left: 5px; width: 255px; background: linear-gradient(135deg, var(--photo-green) 0%, var(--photo-green-dark) 100%); }
  .photo-plant { left: 270px; width: 230px; background: radial-gradient(circle at 50% 60%, var(--photo-green) 0%, var(--photo-green-dark) 100%); }

  .headline-band { position: absolute; left: 5px; right: 0; top: 442px; height: 130px;
    background: linear-gradient(90deg, var(--band-black), var(--band-grey) 50%, var(--band-black));
    border-top: 5px solid var(--green); border-bottom: 5px solid var(--green);
    display: flex; flex-direction: column; justify-content: center; align-items: center;
    font-family: "Roboto Condensed", sans-serif; font-weight: 700; text-transform: uppercase; line-height: 1.05; }
  .headline-top { font-size: 30px; color: var(--headline-grey); }
  .headline-main { font-size: 44px; color: var(--white); }
</style>
</head>
<body>
  <main class="spread">
    <section class="page back-cover">
      <div class="logo-band"><span class="wordmark">KRT</span></div>
      <div class="contact">
        <div class="contact-title">Contact Us</div><br>
        <div class="contact-phone">&#9990; (046)555-0142</div>
        <div class="contact-line"><svg viewBox="0 0 10 10"><rect x="0" y="2" width="10" height="6"/></svg>your@emailid.com</div>
        <div class="contact-line"><svg viewBox="0 0 10 10"><circle cx="5" cy="5" r="5"/></svg>www.yourwebsite.com</div>
        <div class="contact-line"><svg viewBox="0 0 10 10"><path d="M5 0a3.5 3.5 0 0 1 3.5 3.5C8.5 6 5 10 5 10S1.5 6 1.5 3.5A3.5 3.5 0 0 1 5 0z"/></svg>your address</div>
      </div>
      <div class="footer-strip"></div>
    </section>

    <section class="page front-cover">
      <div class="brand-top">
        <span class="wordmark">KRT</span>
        <span class="subname">FERRAVANT</span>
      </div>
      <div class="photo photo-bales" role="img" aria-label="Stacked bales of crushed aluminum cans"></div>
      <div class="photo photo-plant" role="img" aria-label="Cupped hands holding a crushed can with a green sprout"></div>
      <div class="headline-band">
        <span class="headline-top">More Aluminum Recovered</span>
        <span class="headline-main">Less in Your Residue</span>
      </div>
      <div class="footer-strip"></div>
    </section>
  </main>
</body>
</html>
```